Business Card Design Graduates

Slogan
"Practical Skills + Theory = Paid Job"

We assist Accounting Graduates to get work at the end of their University Degree by offering them a 6 week practical experience program.

At completion of the program they get business cards in their own Name, Title, phone numbers, address and email address. So, I need to be able to have a template where I can change these details and purchase business cards via Cardoloom or other outside printers.

I want it to be a bit colourful... ie not a plain white background or black, some blue would be nice. But it also needs to look professional as they will be meeting with future employers and networking. We help them get a paid job in Accounting at completion of the 6 week program.

Target Market(s)

Students and Employers

Industry/Entity Type

Business

Contact Information for Business Card

Marietta Dombrowski, Director, PO Box 418, Kelworth NSW 2174, Phone: 9482-3107 Fax: 9482-5921 Email: mariettad@harrowquill.com.au Web: www.HarrowquillWorkStart.com.au

Requirements
Must have
• changeable fields for me to change details for each student who graduates. The name of the company is already in the logo so no need to duplicate the name. Look at the website www.HarrowquillWorkStart.com.au because we expect the design should match our Corporate Image.

```html
<!DOCTYPE html>
<html lang="en">
<head>
<meta charset="utf-8">
<title>Harrowquill WorkStart – Business Card</title>
<link rel="stylesheet" href="https://fonts.googleapis.com/css2?family=Open+Sans:wght@300;400;600&display=swap">
<style>
  :root {
    --page-bg: #e6e6e6;
    --card-white: #ededed;
    --brand-blue: #1f5fae;
    --logo-blue: #1c4fa0;
    --name-grey: #8c8c8c;
    --panel-dark: #2a2a2a;
    --panel-mid: #3d3d3d;
    --divider-dark: #1e1e1e;
    --divider-silver: #d9d9d9;
    --contact-text: #f4f6fa;
  }
  * { margin: 0; padding: 0; box-sizing: border-box; }
  html, body {
    width: 1200px; height: 900px; overflow: hidden;
    background: var(--page-bg);
    font-family: "Open Sans", Arial, sans-serif;
  }
  .card {
    position: absolute; left: 75px; top: 150px;
    width: 1050px; height: 600px;
    background: var(--card-white);
    overflow: hidden;
    box-shadow: 0 6px 22px rgba(0,0,0,0.18);
  }
  .card__pattern-panel {
    position: absolute; left: 0; top: 0;
    width: 240px; height: 600px;
    background: linear-gradient(135deg, var(--panel-mid) 0%, var(--panel-dark) 45%, #1a1a1a 100%);
  }
  .card__logo {
    position: absolute; left: 330px; top: 95px;
    display: flex; align-items: center; gap: 18px;
  }
  .card__logo-mark {
    width: 40px; height: 40px; border-radius: 50%;
    background: var(--logo-blue);
  }
  .card__logo-name {
    font-size: 56px; font-weight: 400; color: var(--logo-blue);
    letter-spacing: -0.5px; line-height: 1;
  }
  .card__holder {
    position: absolute; left: 272px; top: 225px;
    color: var(--name-grey); font-weight: 300;
    font-size: 46px; line-height: 1.05;
  }
  .card__divider {
    position: absolute; left: 240px; top: 358px;
    width: 810px; height: 12px;
    background: linear-gradient(90deg, var(--divider-silver) 0%, #8a8a8a 30%, var(--divider-dark) 60%, var(--divider-dark) 100%);
  }
  .card__contact-band {
    position: absolute; left: 240px; top: 370px;
    width: 810px; height: 230px;
    background: var(--brand-blue);
    padding: 38px 0 0 36px;
    color: var(--contact-text);
    font-size: 31px; font-weight: 400; line-height: 50px;
  }
</style>
</head>
<body>
  <section class="card" aria-label="Business card">
    <div class="card__pattern-panel" role="img" aria-label="Dark charcoal checkered pattern panel"></div>

    <div class="card__logo">
      <span class="card__logo-mark"></span>
      <span class="card__logo-name">Harrowquill WorkStart</span>
    </div>

    <div class="card__holder">
      <p class="card__holder-name">Marietta Dombrowski</p>
      <p class="card__holder-title">Director</p>
    </div>

    <div class="card__divider"></div>

    <div class="card__contact-band">
      <p class="card__contact-phone">Phone: 9482-3107 Fax: 9482-5921</p>
      <p class="card__contact-email">Email: mariettad@harrowquill.com.au</p>
      <p class="card__contact-web">www.HarrowquillWorkStart.com.au</p>
    </div>
  </section>
</body>
</html>
```